Dental Supplies Company - Email Marketing Campaign

I need a design suitable for email marketing (we use vision 6). We are a dental supply company and I would like to run a promotion on infection control including
- Cleaning Wipes
- Gloves
- Masks
- Sterilisation Monitoring Products

Roughly 6-8 product boxes.

Our website is talvexdentalsupplies.com.au

This will show you our general design layout and colours etc.

```html
<!DOCTYPE html>
<html lang="en">
<head>
<meta charset="utf-8">
<title>Talvex Dental Supplies – Infection Control Essentials Promotion</title>
<link href="https://fonts.googleapis.com/css2?family=Oswald:wght@300;400;500;600;700&family=Lilita+One&family=Rubik:wght@400;500&display=swap" rel="stylesheet">
<style>
  :root {
    --brand-blue: #0b7399;
    --sky: #b6e0e4;
    --gold: #dca220;
    --red: #e8300e;
    --white: #ffffff;
    --shadow: #a3c5ca;
    --ink: #1e2a33;
    --footer-text: #d3e8ef;
  }
  * { box-sizing: border-box; margin: 0; padding: 0; }
  html, body { width: 692px; height: 1200px; overflow: hidden; }
  body { position: relative; background: var(--white); font-family: "Oswald", sans-serif; }
  .abs { position: absolute; }

  /* header */
  .brand { left: 0; width: 692px; top: 22px; display: flex; justify-content: center; align-items: center; gap: 8px; }
  .brand-dot { width: 24px; height: 24px; border-radius: 50%; background: var(--gold); }
  .brand-name { font-family: "Oswald", sans-serif; font-weight: 500; font-size: 22px; color: var(--brand-blue); letter-spacing: .5px; }

  .band { left: 0; width: 692px; background: var(--brand-blue); }
  .perks { left: 0; width: 692px; height: 41px; background: var(--white); display: flex; align-items: center; }
  .perk { width: 115.5px; display: flex; align-items: center; gap: 4px; padding-left: 22px; }
  .perk svg { flex: none; width: 20px; height: 20px; }
  .perk-text { font-family: "Rubik", sans-serif; font-size: 7.4px; line-height: 9.6px; color: var(--ink); white-space: nowrap; }
  .perk-text b { font-weight: 500; }

  /* hero */
  .stage { left: 0; top: 127px; width: 692px; height: 873px; background: var(--sky); }
  .megaphone { width: 110px; height: 132px; border-radius: 50% 45% 40% 50%; background: radial-gradient(circle at 60% 40%, #fde1bd, #f2b36a 55%, #e2953f); }
  .headline { left: 0; width: 692px; text-align: center; color: var(--brand-blue); font-weight: 500; font-size: 45px; line-height: 40px; letter-spacing: .5px; }
  .promo { left: 0; width: 692px; text-align: center; color: var(--gold); font-weight: 700; font-size: 92px; line-height: 80px; letter-spacing: 1px; text-shadow: 2px 3px 0 rgba(120,150,150,.35); }
  .deal { left: 236px; top: 346px; width: 220px; height: 27px; background: var(--red); color: var(--white); font-weight: 600; font-size: 12.5px; line-height: 27px; text-align: center; letter-spacing: .3px; box-shadow: 0 3px 0 rgba(120,150,150,.45); }

  .panel { left: 48px; top: 389px; width: 594px; height: 581px; border: 1.5px solid var(--white); border-radius: 34px; }

  .card { width: 147px; border-radius: 11px; overflow: hidden; background: var(--brand-blue); box-shadow: 6px 6px 0 var(--shadow); }
  .card-photo { margin-top: 12px; width: 100%; background: var(--white); display: flex; align-items: center; justify-content: center; }
  .card-photo > div { width: 82%; height: 78%; border-radius: 6px; }
  .card-label { display: flex; align-items: center; justify-content: center; text-align: center; color: var(--white); }
  .label-bold { font-weight: 600; font-size: 16.5px; letter-spacing: 1.2px; }
  .label-light { font-weight: 400; font-size: 17px; line-height: 18.5px; letter-spacing: .6px; }

  .shop { width: 104px; height: 26px; background: var(--gold); color: var(--white); font-family: "Lilita One", sans-serif; font-size: 15px; line-height: 26px; text-align: center; letter-spacing: .8px; box-shadow: 6px 6px 0 var(--shadow); }

  /* footer */
  .footer { left: 0; top: 1065px; width: 692px; height: 135px; background: var(--brand-blue); text-align: center; padding-top: 28px; font-weight: 300; font-size: 10.6px; line-height: 12.4px; color: var(--footer-text); letter-spacing: .2px; }
  .footer-title { color: var(--gold); font-weight: 600; }
</style>
</head>
<body>

<header class="abs brand">
  <span class="brand-dot"></span>
  <span class="brand-name">Talvex Dental Supplies</span>
</header>

<div class="abs band" style="top:70px;height:8px"></div>
<div class="abs perks" style="top:78px">
  <div class="perk"><svg viewBox="0 0 20 20"><rect x="1" y="6" width="11" height="8" fill="#e8413b"/><path d="M12 9h4l3 3v2h-7z" fill="#e8413b"/><circle cx="5" cy="16" r="2" fill="#e8413b"/><circle cx="15" cy="16" r="2" fill="#e8413b"/><circle cx="6" cy="5" r="4" fill="#e8413b" stroke="#fff"/></svg><div class="perk-text"><b>Orders dispatched</b><br>within 24 hours.</div></div>
  <div class="perk"><svg viewBox="0 0 20 20"><path d="M10 2a6 6 0 0 1 6 6c0 5-6 10-6 10S4 13 4 8a6 6 0 0 1 6-6z" fill="#1c7fb9"/><circle cx="10" cy="8" r="2.2" fill="#fff"/></svg><div class="perk-text"><b>Australian Family</b><br>Owned &amp; Operated</div></div>
  <div class="perk"><svg viewBox="0 0 20 20"><rect x="3" y="2" width="12" height="16" rx="1" fill="#253f7d"/><path d="M6 7h6M6 10h6M6 13h4" stroke="#fff" stroke-width="1.2"/><path d="M14 14l4-7" stroke="#253f7d" stroke-width="2"/></svg><div class="perk-text"><b>Fast, seamless, online</b><br>account applications</div></div>
  <div class="perk"><svg viewBox="0 0 20 20"><rect x="1" y="6" width="11" height="8" fill="#4caf50"/><path d="M12 9h4l3 3v2h-7z" fill="#4caf50"/><circle cx="5" cy="16" r="2" fill="#2e7d32"/><circle cx="15" cy="16" r="2" fill="#2e7d32"/></svg><div class="perk-text"><b>Free shipping</b><br>to most capital cities</div></div>
  <div class="perk"><svg viewBox="0 0 20 20"><rect x="1" y="5" width="12" height="12" fill="#f0b429"/><rect x="4" y="8" width="6" height="5" fill="#fff"/><path d="M16 4a2.5 2.5 0 0 1 2.5 2.5C18.5 9 16 12 16 12s-2.5-3-2.5-5.5A2.5 2.5 0 0 1 16 4z" fill="#f0b429"/></svg><div class="perk-text"><b>Real-Time</b><br>Order Updates</div></div>
  <div class="perk"><svg viewBox="0 0 20 20"><rect x="2" y="2" width="16" height="12" rx="1" fill="none" stroke="#1c7fb9" stroke-width="1.6"/><path d="M5 6h2l1.5 4h5l1-3H8" fill="none" stroke="#1c7fb9" stroke-width="1.2"/><rect x="2" y="16" width="16" height="2" fill="#1c7fb9"/></svg><div class="perk-text"><b>24/7</b><br>online ordering</div></div>
</div>
<div class="abs band" style="top:119px;height:8px"></div>

<main class="abs stage">
  <div class="abs megaphone" role="img" aria-label="Orange megaphone illustration" style="left:40px;top:34px"></div>
  <div class="abs megaphone" role="img" aria-label="Orange megaphone illustration" style="left:542px;top:34px;transform:scaleX(-1)"></div>

  <h1 class="abs headline" style="top:46px;font-size:45px">INFECTION CONTROL<br>ESSENTIALS</h1>
  <div class="abs promo" style="top:129px">PROMOTION</div>
  <div class="abs deal" style="top:219px">SAVE BIG WITH AMAZING SPECIAL DEALS</div>

  <section class="abs panel" style="top:262px"></section>

  <!-- row one -->
  <article class="abs card" style="left:86.5px;top:278px">
    <div class="card-photo" style="height:133px"><div role="img" aria-label="Packs and tubs of cleaning wipes" style="background:linear-gradient(160deg,#e4f3ee,#6cc2a6)"></div></div>
    <div class="card-label label-bold" style="height:44px">CLEANING WIPES</div>
  </article>
  <article class="abs card" style="left:272px;top:278px">
    <div class="card-photo" style="height:133px"><div role="img" aria-label="Blue nitrile glove beside a box of gloves" style="background:linear-gradient(160deg,#7ea9e6,#e8eef8)"></div></div>
    <div class="card-label label-bold" style="height:44px">GLOVES</div>
  </article>
  <article class="abs card" style="left:458px;top:278px">
    <div class="card-photo" style="height:133px;background:#f1f1f1"><div role="img" aria-label="Disposable face mask" style="background:linear-gradient(160deg,#f4f4f4,#c9c9c9)"></div></div>
    <div class="card-label label-bold" style="height:44px">MASKS</div>
  </article>

  <a class="abs shop" style="left:109px;top:492px">SHOP NOW</a>
  <a class="abs shop" style="left:294px;top:492px">SHOP NOW</a>
  <a class="abs shop" style="left:479px;top:492px">SHOP NOW</a>

  <!-- row two -->
  <article class="abs card" style="left:86.5px;top:553px">
    <div class="card-photo" style="height:134px"><div role="img" aria-label="Sterilisation monitoring kit and indicator strips" style="background:linear-gradient(160deg,#2a5d9a,#e9edf3)"></div></div>
    <div class="card-label label-light" style="height:78px">STERILISATION<br>MONITORING<br>PRODUCTS</div>
  </article>
  <article class="abs card" style="left:272px;top:553px">
    <div class="card-photo" style="height:134px"><div role="img" aria-label="Carton and pack of hand towels" style="background:linear-gradient(160deg,#c79b6a,#dfe3e6)"></div></div>
    <div class="card-label label-light" style="height:78px">TOWELS<br>AND<br>TISSUES</div>
  </article>
  <article class="abs card" style="left:458px;top:553px">
    <div class="card-photo" style="height:134px"><div role="img" aria-label="Spray bottle of surface disinfectant" style="background:linear-gradient(180deg,#f2f5f2,#5cb85c)"></div></div>
    <div class="card-label label-light" style="height:78px">SURFACE<br>DISINFECTANTS</div>
  </article>

  <a class="abs shop" style="left:109px;top:801px">SHOP NOW</a>
  <a class="abs shop" style="left:294px;top:801px">SHOP NOW</a>
  <a class="abs shop" style="left:479px;top:801px">SHOP NOW</a>
</main>

<div class="abs band" style="top:1000px;height:10px"></div>
<div class="abs perks" style="top:1010px">
  <div class="perk"><svg viewBox="0 0 20 20"><rect x="1" y="6" width="11" height="8" fill="#e8413b"/><path d="M12 9h4l3 3v2h-7z" fill="#e8413b"/><circle cx="5" cy="16" r="2" fill="#e8413b"/><circle cx="15" cy="16" r="2" fill="#e8413b"/><circle cx="6" cy="5" r="4" fill="#e8413b" stroke="#fff"/></svg><div class="perk-text"><b>Orders dispatched</b><br>within 24 hours.</div></div>
  <div class="perk"><svg viewBox="0 0 20 20"><path d="M10 2a6 6 0 0 1 6 6c0 5-6 10-6 10S4 13 4 8a6 6 0 0 1 6-6z" fill="#1c7fb9"/><circle cx="10" cy="8" r="2.2" fill="#fff"/></svg><div class="perk-text"><b>Australian Family</b><br>Owned &amp; Operated</div></div>
  <div class="perk"><svg viewBox="0 0 20 20"><rect x="3" y="2" width="12" height="16" rx="1" fill="#253f7d"/><path d="M6 7h6M6 10h6M6 13h4" stroke="#fff" stroke-width="1.2"/><path d="M14 14l4-7" stroke="#253f7d" stroke-width="2"/></svg><div class="perk-text"><b>Fast, seamless, online</b><br>account applications</div></div>
  <div class="perk"><svg viewBox="0 0 20 20"><rect x="1" y="6" width="11" height="8" fill="#4caf50"/><path d="M12 9h4l3 3v2h-7z" fill="#4caf50"/><circle cx="5" cy="16" r="2" fill="#2e7d32"/><circle cx="15" cy="16" r="2" fill="#2e7d32"/></svg><div class="perk-text"><b>Free shipping</b><br>to most capital cities</div></div>
  <div class="perk"><svg viewBox="0 0 20 20"><rect x="1" y="5" width="12" height="12" fill="#f0b429"/><rect x="4" y="8" width="6" height="5" fill="#fff"/><path d="M16 4a2.5 2.5 0 0 1 2.5 2.5C18.5 9 16 12 16 12s-2.5-3-2.5-5.5A2.5 2.5 0 0 1 16 4z" fill="#f0b429"/></svg><div class="perk-text"><b>Real-Time</b><br>Order Updates</div></div>
  <div class="perk"><svg viewBox="0 0 20 20"><rect x="2" y="2" width="16" height="12" rx="1" fill="none" stroke="#1c7fb9" stroke-width="1.6"/><path d="M5 6h2l1.5 4h5l1-3H8" fill="none" stroke="#1c7fb9" stroke-width="1.2"/><rect x="2" y="16" width="16" height="2" fill="#1c7fb9"/></svg><div class="perk-text"><b>24/7</b><br>online ordering</div></div>
</div>
<div class="abs band" style="top:1051px;height:8px"></div>

<footer class="abs footer">
  <div class="footer-title">TALVEX DENTAL SUPPLIES</div>
  <div>12 HARLOW STREET, KELVALE, VIC 3099</div>
  <div>CONTACT 1300 555 014</div>
  <div>SALES@TALVEX.COM.AU | TALVEXDENTALSUPPLIES.COM.AU</div>
  <div>YOU RECEIVED THIS EMAIL BECAUSE YOU ARE SUBSCRIBED TO OUR NEWSLETTER.</div>
  <div>VIEW ONLINE | UNSUBSCRIBE</div>
</footer>

</body>
</html>
```